REALTOR POSTCARD HANDOUT

I AM A MORTGAGE COMPANY...THIS WILL BE A HANDOUT ON A LARGE POSTCARD THAT I WILL BE GIVING OUT AT OPEN HOUSES.IT WILL HAVE VARIOUS NICHES THAT I FUND THAT MOST OTHER LENDERS DONT FUND...

Industry/Entity Type

It Company

Logo Text

KVO (STAND FOR KESTREL VALLEY ORCHARD)

Logo styles of interest
Lettermark Logo
Requirements
Must have
• I WANT IT TO BE A VERY BRIGHT AND VIDID POSTCARD...I MIGHT HAVE A MORTGAGE CALUCALTOR ON THE BACK OF THE CARD POSSIBLY....
Nice to have
• LOTS OF COLORS..BUT CLASSY AS WELL..IT WILL BE EMBOSSED
POSSIBLE GRAPHICS..BUT NOT TOO BUSY....

```html
<!DOCTYPE html>
<html lang="en">
<head>
<meta charset="utf-8">
<title>KVO Open House Postcard</title>
<link rel="stylesheet" href="https://fonts.googleapis.com/css2?family=Josefin+Sans:wght@400;600;700&family=Oswald:wght@400&display=swap">
<style>
  :root {
    --orange: #f18a00;
    --ink: #111111;
    --paper: #ffffff;
  }
  * { margin: 0; padding: 0; box-sizing: border-box; }
  html, body { width: 1200px; height: 2424px; overflow: hidden; background: var(--paper); }
  body { position: relative; font-family: "Josefin Sans", sans-serif; color: var(--ink); }

  /* Brand lockup */
  .brand { position: absolute; left: 0; width: 1200px; top: 270px; text-align: center; color: var(--ink); }
  .brand-mark { font-weight: 700; font-size: 250px; line-height: 1; letter-spacing: -4px; }
  .brand-name { font-weight: 700; font-size: 31px; line-height: 1; letter-spacing: 0.5px; margin-top: 14px; }

  /* Front of postcard */
  .card-front { position: absolute; left: 35px; top: 757px; width: 1130px; height: 770px; background: var(--orange); overflow: hidden; }
  .card-front .chevron { position: absolute; left: 0; top: 0; }
  .headline { position: absolute; left: 0; top: 262px; width: 1020px; text-align: center;
    font-family: "Oswald", sans-serif; font-weight: 400; font-size: 150px; line-height: 1.02;
    text-decoration: underline; text-decoration-thickness: 7px; text-underline-offset: 8px; color: var(--ink); }
  .headline span { display: block; }
  .front-brand { position: absolute; left: 1020px; top: 290px; transform-origin: left top; transform: rotate(90deg);
    font-weight: 700; font-size: 92px; line-height: 1; color: var(--ink); white-space: nowrap; }
  .front-brand-name { position: absolute; left: 900px; top: 292px; transform-origin: left top; transform: rotate(90deg);
    font-weight: 700; font-size: 13px; line-height: 1; color: var(--ink); white-space: nowrap; }

  /* Back of postcard */
  .card-back { position: absolute; left: 35px; top: 1600px; width: 1130px; height: 800px; border: 3px solid var(--orange); }
  .back-brand { position: absolute; left: 60px; top: 112px; color: var(--ink); }
  .back-brand .brand-mark { font-size: 120px; letter-spacing: -2px; }
  .back-brand .brand-name { font-size: 16px; margin-top: 4px; letter-spacing: 0.3px; }
  .blurb { position: absolute; left: 115px; top: 266px; width: 410px; font-weight: 700; font-size: 14px; line-height: 19px; color: var(--ink); }
  .cta { position: absolute; left: 110px; top: 448px; font-weight: 600; font-size: 62px; line-height: 1; letter-spacing: 1px; color: var(--orange); }
  .calc-icon { position: absolute; left: 142px; top: 548px; }
  .contact { position: absolute; left: 251px; top: 538px; color: var(--orange); font-size: 15px; line-height: 22px; }
  .contact .name { font-weight: 700; font-size: 19px; margin-bottom: 6px; letter-spacing: 0.5px; }
  .contact li { list-style: none; display: flex; align-items: flex-start; gap: 10px; }
  .contact svg { flex: none; margin-top: 3px; }
  .contact .indent { padding-left: 24px; }
  .web { position: absolute; left: 251px; top: 700px; color: var(--orange); font-weight: 600; font-size: 15px; }
  .divider { position: absolute; left: 564px; top: 105px; width: 3px; height: 596px; background: var(--orange); }
  .stamp-box { position: absolute; left: 909px; top: 105px; width: 153px; height: 153px; border: 3px solid var(--orange); }
</style>
</head>
<body>

  <header class="brand">
    <div class="brand-mark">KVO</div>
    <div class="brand-name">KESTREL VALLEY ORCHARD</div>
  </header>

  <section class="card-front">
    <svg class="chevron" width="1130" height="770" viewBox="0 0 1130 770" aria-hidden="true">
      <polygon points="0,0 90,0 330,385 80,770 0,770 0,705 210,385 0,90" fill="#ffffff"/>
    </svg>
    <h1 class="headline"><span>OPEN HOUSE</span><span>2014</span></h1>
    <div class="front-brand-name">KESTREL VALLEY ORCHARD</div>
    <div class="front-brand">KVO</div>
  </section>

  <section class="card-back">
    <div class="back-brand">
      <div class="brand-mark">KVO</div>
      <div class="brand-name">KESTREL VALLEY ORCHARD</div>
    </div>

    <p class="blurb">Lorem ipsum dolor sit amet, offic tendand itaqui autent etus ut volut pos estrum fugia int rem hil enis quae enectios la dolupta tisquis alia in repudo ipsumlto doloremque et ommolupid everia. Ut sit occuptate earerni scipicis plique sit quatur, sequam, consequat quiducit omnos vellabo rehenia sum liquasp eriuntu sandus doloriorum sequam.</p>

    <div class="cta">CALL TODAY</div>

    <svg class="calc-icon" width="66" height="92" viewBox="0 0 66 92" aria-hidden="true">
      <rect x="2" y="2" width="62" height="88" rx="4" fill="none" stroke="#f18a00" stroke-width="3"/>
      <rect x="10" y="10" width="46" height="18" fill="none" stroke="#f18a00" stroke-width="3"/>
      <g fill="#f18a00">
        <rect x="10" y="36" width="10" height="9"/><rect x="28" y="36" width="10" height="9"/><rect x="46" y="36" width="10" height="9"/>
        <rect x="10" y="52" width="10" height="9"/><rect x="28" y="52" width="10" height="9"/><rect x="46" y="52" width="10" height="9"/>
        <rect x="10" y="68" width="10" height="9"/><rect x="28" y="68" width="10" height="9"/><rect x="46" y="68" width="10" height="9"/>
      </g>
    </svg>

    <div class="contact">
      <div class="name">NADIA FORSYTHE</div>
      <ul>
        <li><svg width="12" height="16" viewBox="0 0 12 16" aria-hidden="true"><path d="M6 0a6 6 0 0 0-6 6c0 4.5 6 10 6 10s6-5.5 6-10a6 6 0 0 0-6-6zm0 8.5a2.5 2.5 0 1 1 0-5 2.5 2.5 0 0 1 0 5z" fill="#f18a00"/></svg><span>42 Linden Crescent,</span></li>
        <li class="indent">Ashby Vale</li>
        <li><svg width="12" height="14" viewBox="0 0 12 14" aria-hidden="true"><path d="M2 0h3l1 4-2 1.5a8 8 0 0 0 4 4L9.5 7.5l3 1v3.5a1.5 1.5 0 0 1-1.5 1.5C5 13.5 0 8 0 2A2 2 0 0 1 2 0z" fill="#f18a00"/></svg><span>0400518273</span></li>
        <li><svg width="12" height="14" viewBox="0 0 12 14" aria-hidden="true"><path d="M2 0h3l1 4-2 1.5a8 8 0 0 0 4 4L9.5 7.5l3 1v3.5a1.5 1.5 0 0 1-1.5 1.5C5 13.5 0 8 0 2A2 2 0 0 1 2 0z" fill="#f18a00"/></svg><span>0881937465</span></li>
        <li><svg width="14" height="14" viewBox="0 0 14 14" aria-hidden="true"><circle cx="7" cy="7" r="5.5" fill="none" stroke="#f18a00" stroke-width="2"/><circle cx="7" cy="7" r="2" fill="#f18a00"/></svg><span>kestrelvalleyorchard@mail.com</span></li>
      </ul>
    </div>

    <div class="web">www.kestrelvalleyorchard.com</div>

    <div class="divider"></div>
    <div class="stamp-box"></div>
  </section>

</body>
</html>
```